Postcard Design January 2015

I need a postcard designed to introduce my company to potential new customers in the UK. My company is TW Page Services based in Chester and we represent one of Poland's leading and long established book printers. We offer competitive pricing, consistently high levels of print and binding quality and industry leading levels of customer service. We have been meeting the print requirements of UK publishers for more than 10 years.
Updates

Industry/Entity Type

Industry

```html
<!DOCTYPE html>
<html lang="en">
<head>
<meta charset="utf-8">
<title>TW Page Services – Postcard</title>
<link rel="stylesheet" href="https://fonts.googleapis.com/css2?family=Oswald:wght@400;500;600&display=swap">
<style>
  :root {
    --page-bg: #d9d9db;
    --ink-black: #0b0b0b;
    --brand-yellow: #d2bf1c;
    --text-yellow: #dcc41b;
    --type-slate: #3c4550;
    --type-teal: #2f5566;
    --type-dark: #1c2026;
  }
  * { margin: 0; padding: 0; box-sizing: border-box; }
  html, body {
    width: 1200px;
    height: 996px;
    overflow: hidden;
    background: var(--page-bg);
    font-family: "Oswald", sans-serif;
  }
  .canvas {
    position: relative;
    width: 1200px;
    height: 996px;
  }
  .postcard {
    position: absolute;
    left: 50px;
    top: 109px;
    width: 1100px;
    height: 777px;
    overflow: hidden;
    background: var(--type-dark);
  }
  .postcard__photo {
    position: absolute;
    inset: 0;
    background:
      radial-gradient(ellipse at 30% 70%, rgba(47, 85, 102, 0.75) 0%, rgba(47, 85, 102, 0) 45%),
      radial-gradient(ellipse at 80% 20%, rgba(80, 100, 125, 0.7) 0%, rgba(80, 100, 125, 0) 50%),
      linear-gradient(135deg, var(--type-slate) 0%, var(--type-dark) 55%, #2a3038 100%);
  }
  .title-band {
    position: absolute;
    left: 0;
    top: 156px;
    width: 710px;
    height: 109px;
    background: rgba(210, 191, 28, 0.92);
    display: flex;
    align-items: center;
    justify-content: center;
    padding-left: 130px;
  }
  .title-band__name {
    font-weight: 600;
    font-size: 62px;
    letter-spacing: 0.5px;
    color: var(--ink-black);
    text-transform: uppercase;
  }
  .service-band {
    position: absolute;
    left: 0;
    top: 265px;
    width: 710px;
    height: 111px;
    background: rgba(10, 10, 10, 0.55);
    display: flex;
    align-items: center;
    justify-content: center;
    padding-left: 130px;
    padding-bottom: 24px;
  }
  .service-band__list {
    font-size: 25px;
    font-weight: 400;
    color: var(--text-yellow);
    text-transform: uppercase;
  }
  .contact-band {
    position: absolute;
    left: 0;
    bottom: 0;
    width: 100%;
    height: 202px;
    background: rgba(5, 5, 5, 0.9);
    text-align: center;
    color: var(--text-yellow);
    padding-top: 22px;
  }
  .contact-band__tagline {
    font-size: 58px;
    font-weight: 500;
    line-height: 1.1;
  }
  .contact-band__line {
    font-size: 22px;
    font-weight: 500;
    line-height: 1.45;
  }
  .contact-band__line:first-of-type { margin-top: 14px; }
</style>
</head>
<body>
<main class="canvas">
  <section class="postcard">
    <div class="postcard__photo" role="img" aria-label="Close-up photograph of worn metal letterpress type blocks in slate and teal tones"></div>

    <div class="title-band">
      <h1 class="title-band__name">TW Page Services</h1>
    </div>

    <div class="service-band">
      <p class="service-band__list">Litho &amp; digital printing, bookbinding &amp; finishing</p>
    </div>

    <footer class="contact-band">
      <p class="contact-band__tagline">book printing made easy</p>
      <p class="contact-band__line">Phone: 01632 960481 • Mobile: 07700 900372</p>
      <p class="contact-band__line">www.twpageservices.co.uk • tomwalsh@twpageservices.co.uk</p>
    </footer>
  </section>
</main>
</body>
</html>
```